Spray Foam Company Business Card

We need a business card designed for our spray foam insulation and roof coatings business. We handle residential and commercial projects.
Construction
We would like it to say:
R & K Spray
with these bullet points
-foam insulation
-waterproofing roof system
-water proofing foundation systems
website is rksprayfoaminsulation.example (this was just purchased)
office phone : 630-482-9164
And 3 cards with names on them the names are :
Derek Halvorsen
Curtis Pennington
Rob Stallworth
maybe the bullet points can go on the back?
if you go this website it is another division of our company and you can see the font we use in the R & K. We do not want to use the same half circles that it has just the lettering
www.coatedrightforyears.example

```html
<!DOCTYPE html>
<html lang="en">
<head>
<meta charset="utf-8">
<title>R &amp; K Spray – Business Card</title>
<link rel="stylesheet" href="https://fonts.googleapis.com/css2?family=Montserrat:wght@600;700&family=Questrial&family=Roboto:wght@400;700&display=swap">
<style>
  :root {
    --frame: #45372d;
    --paper: #fdfdfd;
    --sand: #e5ddc1;
    --coral: #e4604a;
    --gold: #eca33a;
    --ink: #2e2e2e;
    --muted: #4a4a4a;
    --faint: #f4efdf;
    --label: #222222;
  }
  * { box-sizing: border-box; margin: 0; padding: 0; }
  html, body {
    width: 1200px;
    height: 430px;
    overflow: hidden;
    background: #ffffff;
  }
  .sheet {
    position: relative;
    width: 1200px;
    height: 430px;
  }
  .card {
    position: absolute;
    top: 38px;
    width: 549px;
    height: 322px;
    background: var(--frame);
    padding: 18px;
  }
  .card--front { left: 49px; }
  .card--back { left: 607px; }
  .card__face {
    position: relative;
    width: 100%;
    height: 100%;
    overflow: hidden;
  }
  .card--front .card__face { background: var(--paper); }
  .card--back .card__face { background: var(--sand); }

  .accent-band {
    position: absolute;
    right: 0;
    width: 270px;
    height: 14px;
  }
  .accent-band--top { top: 0; }
  .accent-band--bottom { bottom: 0; }

  .brand {
    position: absolute;
    left: 28px;
    top: 58px;
    width: 170px;
    display: flex;
    flex-direction: column;
    align-items: center;
    font-family: "Montserrat", sans-serif;
    font-weight: 700;
    color: var(--gold);
    line-height: 1;
  }
  .brand__mark { font-size: 58px; letter-spacing: 1px; }
  .brand__word { font-size: 30px; letter-spacing: 3px; margin-top: 18px; }

  .contact {
    position: absolute;
    right: 15px;
    top: 96px;
    text-align: right;
  }
  .contact__name {
    font-family: "Montserrat", sans-serif;
    font-weight: 700;
    font-size: 22px;
    letter-spacing: 1.4px;
    color: var(--ink);
  }
  .contact__web, .contact__phone {
    font-family: "Questrial", sans-serif;
    font-size: 15.5px;
    letter-spacing: 0.8px;
    color: var(--muted);
  }
  .contact__web { margin-top: 12px; }
  .contact__phone { margin-top: 14px; }

  .services {
    position: absolute;
    left: 48px;
    top: 62px;
    font-family: "Questrial", sans-serif;
    color: var(--ink);
  }
  .services__title {
    font-family: "Roboto", sans-serif;
    font-weight: 700;
    font-size: 20px;
    margin-bottom: 22px;
  }
  .services__list {
    list-style: none;
    margin-left: -18px;
  }
  .services__item {
    font-size: 17.5px;
    letter-spacing: 0.3px;
    height: 42px;
    display: flex;
    align-items: center;
  }
  .services__item::before {
    content: "";
    width: 7px;
    height: 7px;
    border-radius: 50%;
    background: var(--ink);
    margin-right: 8px;
  }

  .brand--faint {
    left: 360px;
    top: 78px;
    width: 140px;
    color: var(--faint);
  }
  .brand--faint .brand__mark { font-size: 46px; }
  .brand--faint .brand__word { font-size: 22px; margin-top: 16px; }

  .side-label {
    position: absolute;
    top: 375px;
    font-family: "Roboto", sans-serif;
    font-size: 17px;
    color: var(--label);
    transform: translateX(-50%);
  }
  .side-label--front { left: 324px; }
  .side-label--back { left: 841px; top: 378px; }
</style>
</head>
<body>
<main class="sheet">
  <section class="card card--front" aria-label="Business card front">
    <div class="card__face">
      <svg class="accent-band accent-band--top" viewBox="0 0 270 14" preserveAspectRatio="none" aria-hidden="true">
        <polygon points="0,0 270,0 270,14 14,14" fill="var(--coral)"/>
      </svg>
      <div class="brand">
        <span class="brand__mark">R &amp; K</span>
        <span class="brand__word">SPRAY</span>
      </div>
      <div class="contact">
        <p class="contact__name">Curtis Pennington</p>
        <p class="contact__web">rksprayfoaminsulation.example</p>
        <p class="contact__phone">O : 630-482-9164</p>
      </div>
      <svg class="accent-band accent-band--bottom" viewBox="0 0 270 14" preserveAspectRatio="none" aria-hidden="true">
        <polygon points="14,0 270,0 270,14 0,14" fill="var(--coral)"/>
      </svg>
    </div>
  </section>

  <section class="card card--back" aria-label="Business card back">
    <div class="card__face">
      <div class="services">
        <h2 class="services__title">Our Works :</h2>
        <ul class="services__list">
          <li class="services__item">Foam Insulation</li>
          <li class="services__item">Waterproofing Roof System</li>
          <li class="services__item">Water Proofing Foundation Systems</li>
        </ul>
      </div>
      <div class="brand brand--faint" aria-hidden="true">
        <span class="brand__mark">R &amp; K</span>
        <span class="brand__word">SPRAY</span>
      </div>
    </div>
  </section>

  <p class="side-label side-label--front">Front Side</p>
  <p class="side-label side-label--back">Back Side</p>
</main>
</body>
</html>
```